Business Card Design Project

I am looking for a simple business card. I have a logo which I love and have attached. I just need the card to include the logo and the following:
Wanda Pellering
Health & Lifestyle Coach
614/352-8097
wanda@nurtureandmendnation.example
www.pledgetomend.example
Updates
Thank you all for your time and designs, they are great! I chose the business card design that I fell in love with at first sight! Thanks again!
Target Market(s)
businesses looking for corporate wellness.
Industry/Entity Type
Business
Look and feel
Each slider illustrates characteristics of the customer's brand and the style your logo design should communicate.

```html
<!DOCTYPE html>
<html lang="en">
<head>
<meta charset="utf-8">
<title>Pledge to Mend – Business Card</title>
<link rel="stylesheet" href="https://fonts.googleapis.com/css2?family=Arimo:wght@400&display=swap">
<style>
  :root {
    --page-bg: #ece9e4;
    --card-white: #ffffff;
    --green-light: #6cac3a;
    --green-mid: #5a9a2c;
    --green-dark: #3f7c1c;
    --ink: #111111;
    --ink-soft: #6b6b6b;
    --brand-green: #4e8f25;
    --back-mark: rgba(190, 225, 160, 0.38);
  }
  * { box-sizing: border-box; margin: 0; padding: 0; }
  html, body {
    width: 1200px;
    height: 1080px;
    overflow: hidden;
    background: var(--page-bg);
    font-family: "Arimo", Arial, sans-serif;
  }
  .sheet {
    position: relative;
    width: 1200px;
    height: 1080px;
  }
  .card {
    position: absolute;
    left: 235px;
    width: 730px;
    height: 420px;
    border-radius: 26px;
    overflow: hidden;
    box-shadow: 0 6px 18px rgba(0, 0, 0, 0.18);
  }
  .card-front {
    top: 60px;
    background: var(--card-white);
  }
  .card-back {
    top: 600px;
    background: radial-gradient(ellipse at 55% 40%, var(--green-light) 0%, var(--green-mid) 45%, var(--green-dark) 100%);
  }
  .brand {
    position: absolute;
    top: 70px;
    right: 40px;
    display: flex;
    align-items: center;
    gap: 12px;
  }
  .brand-dot {
    width: 22px;
    height: 22px;
    border-radius: 50%;
    background: var(--brand-green);
  }
  .brand-name {
    font-size: 30px;
    color: var(--brand-green);
    letter-spacing: 0.5px;
  }
  .accent-tab {
    position: absolute;
    left: 0;
    top: 210px;
    width: 58px;
    height: 205px;
    border-radius: 0 16px 16px 0;
    background: linear-gradient(180deg, var(--green-light) 0%, var(--green-dark) 100%);
  }
  .contact {
    position: absolute;
    left: 82px;
    top: 212px;
  }
  .person-name {
    font-size: 24px;
    color: var(--ink);
    line-height: 1.2;
  }
  .person-role {
    font-size: 24px;
    color: var(--ink-soft);
    line-height: 1.25;
    margin-bottom: 26px;
  }
  .contact-line {
    font-size: 17px;
    color: var(--ink);
    line-height: 1.3;
  }
  .back-mark {
    position: absolute;
    left: 0;
    right: 0;
    top: 0;
    bottom: 0;
    display: flex;
    align-items: center;
    justify-content: center;
    font-size: 72px;
    color: var(--back-mark);
    letter-spacing: 2px;
  }
</style>
</head>
<body>
  <main class="sheet">
    <section class="card card-front" aria-label="Business card front">
      <div class="brand">
        <span class="brand-dot" aria-hidden="true"></span>
        <span class="brand-name">Pledge to Mend</span>
      </div>
      <div class="accent-tab" aria-hidden="true"></div>
      <div class="contact">
        <p class="person-name">Wanda Pellering</p>
        <p class="person-role">Health &amp; Lifestyle Coach</p>
        <p class="contact-line">614/352-8097</p>
        <p class="contact-line">wanda@nurtureandmendnation.example</p>
        <p class="contact-line">www.pledgetomend.example</p>
      </div>
    </section>

    <section class="card card-back" aria-label="Business card back">
      <div class="back-mark">Pledge to Mend</div>
    </section>
  </main>
</body>
</html>
```